Award winning Indie press looking for a world class book cover for global relaunch

We need to update a book cover for one of our titles which is being relaunched. The title will exist in both physical and e-formats.
There are two primary targets for this book:
1- the coming of age story coupled with the element of forbidden love between a local boy and a British girl
2- the political division of a British colony in the 1950's
Size: A5
Spine: .777 inches or 19.73mm
Title: Thither and Yonder (you may substitute 'and' with '&')
Author: Theodoros K. Lambrakidis
Translated by Marion Ashcombe-Lyle
Blurb: You see before you the entire social mosaic of Cyprus in the ‘50s. - Kathimerinos Logos
Publisher: logo- provided
Back cover text:
The touching story of a teenager who struggles with the eternal problems of adolescence, Thither & Yonder is a coming-of-age novel set in a politically divided country.
While the era of British colonialism in Cyprus is coming to a violent end, Dimitri tries to come to terms with the consequences of the political turmoil on his own life. Strengthened by his passion for medieval poetry and his love for the history of his island, he sets out to balance the Cypriot and English elements in his daily life. His quest for answers is complicated by romantic love for his British friend Anne and his physical attraction to his father’s maid Phrossou. Balancing between different identities, religion and communities, his personal search becomes symbolic of his country’s turbulent political situation.
A nostalgic story about family, love and friendship, Thither & Yonder is a powerful novel about the psychology of an adolescent torn between different worlds, and about the complexities of life and love in the social and historical mosaic of 1950’s colonial Cyprus. It is a beautifully-observed, historically-informed novel by the celebrated Greek historian and novelist.
Other: Please allow a box of approximately 2cm height X 3 cm length for the bar code.
Updates
Hi
I've added two images that could be of some help to you.
Hope they help.
Reason: Appreciating the specific difficulties of this design, it's best to have a few more days
Hi
Please amend front cover blurb to the following:
"This is a novel to be read in one go. A charming narrative…and unexpected turns. It keeps the reader in constant suspense". Pyxida Monthly Literary Review
Target Market(s)
1 - Adults reading coming of age novels
2 - Adults reading historical fiction on British colonialism
Industry/Entity Type
Political
Colors
Designer to choose colors to be used in the design.
Look and feel
Each slider illustrates characteristics of the customer's brand and the style your logo design should communicate.

```html
<!DOCTYPE html>
<html lang="en">
<head>
<meta charset="utf-8">
<title>Thither and Yonder — Front Cover</title>
<link href="https://fonts.googleapis.com/css2?family=Cormorant+Garamond:ital,wght@0,400;0,500;1,400;1,500&family=Cormorant+SC:wght@500&display=swap" rel="stylesheet">
<style>
  :root {
    --paper: #f7f7f6;
    --ink: #151515;
    --ink-soft: #2b2b2b;
    --sepia-light: #f3e6c4;
    --sepia-mid: #d8be86;
    --sepia-deep: #6e5a3a;
    --haze: #fbf7ee;
  }
  html, body {
    margin: 0;
    padding: 0;
    width: 900px;
    height: 1200px;
    overflow: hidden;
    background: var(--paper);
  }
  .cover {
    position: relative;
    width: 900px;
    height: 1200px;
    background: var(--paper);
    color: var(--ink);
    font-family: "Cormorant Garamond", Georgia, serif;
  }
  .title-block {
    position: absolute;
    top: 205px;
    left: 0;
    width: 820px;
    text-align: center;
  }
  .title {
    margin: 0;
    font-weight: 400;
    line-height: 1;
  }
  .title__word {
    display: block;
    font-size: 84px;
    letter-spacing: 0.14em;
    text-transform: uppercase;
  }
  .title__joiner {
    display: block;
    font-style: italic;
    font-size: 40px;
    margin: 10px 0 12px;
  }
  .title-rule {
    display: block;
    margin: 24px auto 0;
  }
  .author {
    position: absolute;
    top: 480px;
    left: 0;
    width: 820px;
    margin: 0;
    text-align: center;
    font-style: italic;
    font-weight: 500;
    font-size: 46px;
    letter-spacing: 0.14em;
  }
  .translator {
    position: absolute;
    top: 560px;
    left: 0;
    width: 820px;
    margin: 0;
    text-align: center;
    font-style: italic;
    font-size: 19px;
    letter-spacing: 0.14em;
    color: var(--ink-soft);
  }
  .cover-photo {
    position: absolute;
    top: 640px;
    left: 0;
    width: 900px;
    height: 340px;
    background:
      linear-gradient(180deg, var(--paper) 0%, var(--sepia-light) 12%, var(--haze) 30%, var(--sepia-mid) 62%, var(--sepia-deep) 78%, var(--sepia-light) 92%, var(--paper) 100%);
  }
  .review {
    position: absolute;
    top: 1010px;
    right: 50px;
    width: 640px;
    margin: 0;
    text-align: right;
  }
  .review__quote {
    margin: 0;
    font-style: italic;
    font-size: 24px;
    line-height: 1.3;
    color: var(--ink-soft);
  }
  .review__source {
    display: block;
    margin-top: 4px;
    font-family: "Cormorant SC", Georgia, serif;
    font-style: normal;
    font-size: 22px;
    letter-spacing: 0.06em;
    color: var(--ink-soft);
  }
</style>
</head>
<body>
  <main class="cover">
    <header class="title-block">
      <h1 class="title">
        <span class="title__word">Thither</span>
        <span class="title__joiner">and</span>
        <span class="title__word">Yonder</span>
      </h1>
      <svg class="title-rule" width="460" height="10" viewBox="0 0 460 10" aria-hidden="true">
        <line x1="5" y1="5" x2="455" y2="5" stroke="#151515" stroke-width="2.5"/>
        <circle cx="5" cy="5" r="4" fill="#151515"/>
        <circle cx="455" cy="5" r="4" fill="#151515"/>
      </svg>
    </header>

    <p class="author">Theodoros K. Lambrakidis</p>
    <p class="translator">Translated by Marion Ashcombe-Lyle</p>

    <div class="cover-photo" role="img" aria-label="Sepia photograph of two old bicycles with front baskets parked side by side in soft hazy light"></div>

    <blockquote class="review">
      <p class="review__quote">"This is a novel to be read in one go. A charming narrative…<br>and unexpected turns. It keeps the reader in constant suspense."</p>
      <cite class="review__source">Pyxida Monthly Literary Review</cite>
    </blockquote>
  </main>
</body>
</html>
```